Global VPN service needs mobile app design

The following design assets are required for a new mobile app called BrambleLink, that allows its users to anonymously use torrent sites for faster & secure downloads without anyone being able to trace the torrent download back to the users device or IP address:
1. App Logo/Icon - Main app logo/icon that will be used in the app home page, app store postings etc. Should represent the 'BrambleLink' name along with the fast, anonymised and secure torrent download capabilities of the app. The name may or may not be part of the logo - open to new ideas and recommendations. Please also incorporate design elements from one or more of the following torrent icons into our icon/logo as the BrambleLink app is primarily targeted at users who regularly use their devices for torrent downloads:
http://www.glyphshelf.example/show/pebblecut-icons-by-marovin/Apps-Kettle-icon.html
http://www.glyphshelf.example/show/lanternfold-icons-by-pirswald7th/Media-okettle-icon.html
http://www.glyphshelf.example/show/kettle-icons-by-oru-dyne/pkettle-icon.html
2. App UI Schema - App home page with a simple background representing a fast & secure connection for torrent downloads along with status icons to show the
VPN connection status (Connected or Disconnected).
3. Splash Screen - Usually a simple screen with just the icon on a suitable background (plain color coordinated or a relevant image)
You can find info on some popular BrambleLink apps here:
http://www.tunnelgrades.example/tunnel-providers/kettle-tunnel-2/?kw=kettle%20tunnel&gclid=QXRm7pb-8L2WGhqTzNuf4K9PWa
https://www.primetunnel.example/prime-tunnel-kettling/
http://www.bramblelink.example/
More info on the top torrent sites are can be found here:
https://kettlegazette.example/top-10-most-visited-kettle-hubs-of-2016-160102/
Industry/Entity Type
It Service
Look and feel
Each slider illustrates characteristics of the customer's brand and the style your logo design should communicate.

```html
<!DOCTYPE html>
<html lang="en">
<head>
<meta charset="utf-8">
<title>BrambleLink – App Screen</title>
<link rel="stylesheet" href="https://fonts.googleapis.com/css2?family=Exo+2:wght@400&family=Source+Sans+3:wght@400;600&display=swap">
<style>
  :root {
    --bg-light: #ededed;
    --bg-dark: #c4c4c4;
    --bar: #5b5b5b;
    --bar-text: #ffffff;
    --panel: #e7e7e7;
    --rule: #9a9a9a;
    --ink: #2b2b2b;
    --ink-soft: #555555;
    --accent: #0a8fb4;
    --ring-track: #c9c9c9;
    --row: #b7d7de;
    --location: #d2d2d2;
    --frame: #3a3a3a;
    --brand-grey: #8f9093;
    --brand-text: #77787b;
  }
  * { box-sizing: border-box; margin: 0; padding: 0; }
  html, body { width: 1200px; height: 900px; overflow: hidden; }
  body {
    position: relative;
    background: linear-gradient(100deg, var(--bg-dark) 0%, var(--bg-light) 55%, var(--bg-light) 100%);
    font-family: "Source Sans 3", sans-serif;
    color: var(--ink);
  }

  /* ---------- App screen ---------- */
  .app-screen {
    position: absolute; left: 254px; top: 174px;
    width: 310px; height: 550px;
    background: var(--panel);
    border: 2px solid var(--frame);
    overflow: hidden;
  }
  .app-bar { position: absolute; left: 0; top: 0; width: 100%; height: 83px; background: var(--bar); color: var(--bar-text); }
  .app-bar__back { position: absolute; left: 12px; top: 12px; }
  .app-bar__title { position: absolute; left: 0; right: 0; top: 9px; text-align: center; font-size: 19px; }
  .app-bar__menu { position: absolute; right: 18px; top: 14px; }
  .app-tabs { position: absolute; left: 0; top: 43px; width: 100%; height: 40px; display: flex; }
  .app-tabs__item { font-size: 17px; display: flex; align-items: center; justify-content: center; border-right: 1px solid #7a7a7a; }
  .app-tabs__item:last-child { border-right: 0; }
  .app-tabs__item--all { width: 78px; }
  .app-tabs__item--download { width: 116px; border-bottom: 4px solid #d7d7d7; }
  .app-tabs__item--complete { flex: 1; }

  .stats { position: absolute; left: 0; top: 83px; width: 100%; height: 181px; background: var(--panel); box-shadow: 0 3px 4px rgba(0,0,0,0.12); }
  .stat { position: absolute; width: 97px; border-top: 1px solid var(--rule); padding-top: 2px; }
  .stat__label { font-size: 9px; color: var(--ink-soft); letter-spacing: 0.2px; }
  .stat__value { font-size: 12px; line-height: 14px; }
  .stat__value small { font-size: 9px; }
  .stat--seeds { left: 13px; top: 42px; }
  .stat--peers { left: 13px; top: 114px; }
  .stat--speed { left: 200px; top: 42px; }
  .stat--seeds-right { left: 200px; top: 114px; }
  .progress-ring { position: absolute; left: 110px; top: 45px; }

  .detail-tabs { position: absolute; left: 0; top: 264px; width: 100%; height: 30px; display: flex; font-size: 13px; }
  .detail-tabs__item { display: flex; align-items: center; justify-content: center; }
  .detail-tabs__item--files { width: 153px; background: #ffffff; }
  .detail-tabs__item--details { flex: 1; background: var(--accent); color: #ffffff; }

  .file-row { position: absolute; left: 0; top: 294px; width: 100%; height: 83px; background: var(--row); }
  .file-row__ring { position: absolute; left: 12px; top: 14px; }
  .file-row__name { position: absolute; left: 88px; top: 31px; font-size: 13px; }

  .download-location { position: absolute; left: 19px; top: 407px; width: 270px; height: 56px; background: var(--location); }
  .download-location__icon { position: absolute; left: 19px; top: 20px; }
  .download-location__title { position: absolute; left: 61px; top: 12px; font-size: 13px; }
  .download-location__path { position: absolute; left: 61px; top: 29px; font-size: 10.5px; color: var(--ink-soft); }

  /* ---------- Brand ---------- */
  .brand-mark { position: absolute; left: 799px; top: 58px; width: 216px; height: 216px; border-radius: 50%; background: var(--brand-grey); }
  .brand-name {
    position: absolute; left: 688px; top: 308px; width: 428px;
    font-family: "Exo 2", sans-serif; font-weight: 400;
    font-size: 62px; letter-spacing: 3px; color: var(--brand-text);
    text-align: center;
  }
</style>
</head>
<body>

<main class="app-screen">
  <header class="app-bar">
    <svg class="app-bar__back" width="26" height="22" viewBox="0 0 26 22" aria-hidden="true">
      <path d="M11 2 L2 11 L11 20 M3 11 H24" fill="none" stroke="#fff" stroke-width="4" stroke-linejoin="miter"/>
    </svg>
    <h1 class="app-bar__title">BrambleLink</h1>
    <svg class="app-bar__menu" width="6" height="22" viewBox="0 0 6 22" aria-hidden="true">
      <rect x="1" y="1" width="4" height="4" fill="#fff"/>
      <rect x="1" y="9" width="4" height="4" fill="#fff"/>
      <rect x="1" y="17" width="4" height="4" fill="#fff"/>
    </svg>
    <nav class="app-tabs">
      <span class="app-tabs__item app-tabs__item--all">All</span>
      <span class="app-tabs__item app-tabs__item--download">Download</span>
      <span class="app-tabs__item app-tabs__item--complete">Complete</span>
    </nav>
  </header>

  <section class="stats">
    <div class="stat stat--seeds">
      <div class="stat__label">SEEDS</div>
      <div class="stat__value">0 <small>/ 152</small></div>
    </div>
    <div class="stat stat--peers">
      <div class="stat__label">PEERS</div>
      <div class="stat__value">0 <small>/ 534</small></div>
    </div>
    <div class="stat stat--speed">
      <div class="stat__label">SPEED</div>
      <div class="stat__value">&#8595; 0 B/s</div>
      <div class="stat__value">&#8593; 0 B/s</div>
    </div>
    <div class="stat stat--seeds-right">
      <div class="stat__label">SEEDS</div>
      <div class="stat__value">0 <small>/ 152</small></div>
    </div>
    <svg class="progress-ring" width="86" height="86" viewBox="0 0 86 86" aria-label="75% downloaded">
      <circle cx="43" cy="43" r="39" fill="none" stroke="var(--ring-track)" stroke-width="4"/>
      <circle cx="43" cy="43" r="39" fill="none" stroke="var(--accent)" stroke-width="4"
              stroke-dasharray="183.8 245" transform="rotate(-90 43 43)"/>
      <text x="43" y="52" text-anchor="middle" font-family="Source Sans 3, sans-serif" font-size="26" fill="#2b2b2b">75%</text>
    </svg>
  </section>

  <nav class="detail-tabs">
    <span class="detail-tabs__item detail-tabs__item--files">FILES</span>
    <span class="detail-tabs__item detail-tabs__item--details">DETAILS</span>
  </nav>

  <section class="file-row">
    <svg class="file-row__ring" width="56" height="56" viewBox="0 0 56 56" aria-label="75% downloaded">
      <circle cx="28" cy="28" r="25" fill="none" stroke="var(--ring-track)" stroke-width="3"/>
      <circle cx="28" cy="28" r="25" fill="none" stroke="var(--accent)" stroke-width="3"
              stroke-dasharray="117.8 157.1" transform="rotate(-90 28 28)"/>
      <text x="28" y="34" text-anchor="middle" font-family="Source Sans 3, sans-serif" font-size="16" fill="#2b2b2b">75%</text>
    </svg>
    <span class="file-row__name">BrambleLink.apk</span>
  </section>

  <section class="download-location">
    <svg class="download-location__icon" width="20" height="16" viewBox="0 0 20 16" aria-hidden="true">
      <path d="M0 1 H7 L9 3 H20 V16 H0 Z" fill="#555"/>
    </svg>
    <div class="download-location__title">Download Location</div>
    <div class="download-location__path">/storage/emulated/0/Download</div>
  </section>
</main>

<div class="brand-mark" aria-hidden="true"></div>
<div class="brand-name">BrambleLink</div>

</body>
</html>
```